Engineering Consultant Business Card

I'm starting a new business as a high-end engineering consultant in a niche field. I've attached the jpg for my logo plus the branding guideline document that I've been following. You can see my business website here: www.tarvikworks.com
I'd like a business card that has the logo on one side, then the other side has (in any order): Tarvik Works, Inc.
Dana Whitlock
President and Chief EMC Engineer
www.tarvikworks.com
dana@tarvikworks.com
Optional: motto "We will solve your EMC problems as early as possible—ideally before they even start."
I'm not planning on including a phone number
Target Market(s)
Businesses, especially makers of electronics hardware
Industry/Entity Type
Electrical engineering
Contact Information for Business Card
Company name, my name, website, email

```html
<!DOCTYPE html>
<html lang="en">
<head>
<meta charset="utf-8">
<title>Tarvik Works, Inc. — Business Card</title>
<link rel="stylesheet" href="https://fonts.googleapis.com/css2?family=Inter:wght@600;700&family=Noto+Serif:wght@400;700&display=swap">
<style>
  :root {
    --brand-blue: #2f4696;
    --card-light: #eaf7f8;
    --backdrop: #a3a5aa;
  }
  * { margin: 0; padding: 0; box-sizing: border-box; }
  html, body {
    width: 1200px;
    height: 1200px;
    overflow: hidden;
    background: var(--backdrop);
  }
  .canvas {
    position: relative;
    width: 1200px;
    height: 1200px;
  }
  .card {
    position: absolute;
    left: 190px;
    width: 819px;
    height: 470px;
    overflow: hidden;
  }
  .card-front {
    top: 90px;
    background: var(--card-light);
  }
  .card-back {
    top: 624px;
    background: var(--brand-blue);
    color: var(--card-light);
  }
  .front-bands {
    position: absolute;
    inset: 0;
  }
  .wordmark {
    position: absolute;
    left: 302px;
    top: 235px;
    transform: translate(-50%, -50%);
    display: flex;
    align-items: center;
    gap: 22px;
    color: var(--brand-blue);
    font-family: "Inter", sans-serif;
    font-weight: 700;
    font-size: 64px;
    line-height: 1;
    letter-spacing: 1px;
  }
  .wordmark-dot {
    width: 56px;
    height: 56px;
    border: 10px solid var(--brand-blue);
    border-radius: 50%;
    flex: none;
  }
  .company-name,
  .person-name {
    position: absolute;
    left: 48px;
    font-family: "Inter", sans-serif;
    font-weight: 700;
    font-size: 56px;
    line-height: 1;
    letter-spacing: -0.5px;
  }
  .company-name { top: 51px; }
  .person-name { top: 233px; }
  .name-rule {
    position: absolute;
    left: 50px;
    top: 294px;
    width: 351px;
    height: 3px;
    background: var(--card-light);
  }
  .contact {
    position: absolute;
    left: 48px;
    font-family: "Noto Serif", serif;
    line-height: 1;
    white-space: nowrap;
  }
  .job-title { top: 309px; font-size: 20px; }
  .email { top: 358px; font-size: 25px; }
  .website { top: 393px; font-size: 25px; font-weight: 700; }
</style>
</head>
<body>
<main class="canvas">
  <section class="card card-front" aria-label="Business card front">
    <svg class="front-bands" width="819" height="470" viewBox="0 0 819 470" aria-hidden="true">
      <path d="M565 0 Q725 235 565 470 L603 470 Q755 235 603 0 Z" fill="var(--brand-blue)"/>
      <path d="M638 0 Q784 235 638 470 L819 470 L819 0 Z" fill="var(--brand-blue)"/>
    </svg>
    <div class="wordmark">
      <span class="wordmark-dot"></span>
      <span class="wordmark-text">TARVIK</span>
    </div>
  </section>

  <section class="card card-back" aria-label="Business card back">
    <h1 class="company-name">Tarvik Works, Inc.</h1>
    <h2 class="person-name">Dana Whitlock</h2>
    <div class="name-rule"></div>
    <p class="contact job-title">President and Chief EMC Engineer</p>
    <p class="contact email">dana@tarvikworks.com</p>
    <p class="contact website">www.tarvikworks.com</p>
  </section>
</main>
</body>
</html>
```